Recruitment company website redesign

We're looking to redesign our current website, located at http://www.crew4crew.com.au, to make it more FRESH, modern, easy-to-navigate, and user-friendly. Navigation should be very obvious, and buttons should be big. The design should be closer to the flat/clean look of Plovix or Vuma9 rather than the somewhat older embossed look.

The design also needs to take into consideration that the coding will be responsive (mobile, tablet, etc.-friendly).

We'd like to see your work on two pages, and from there, we'll choose a designer that we will pay further to design the rest of the site. The two pages we will need are:

1. A home page, with the content detailed in the attached image home-outline.jpg. Keep in mind that this is a very rough outline with no design whatsoever, so please take those elements and create a beautiful page from it. Feel free to move the content around if necessary, as long as that's all on there. We're pretty open to whatever you think would look best.

Using high quality images could look great, and we'd purchase the perfect stock photos down the line, but for now just use any business-related images that aren't too cheesy (stay away from anything that looks too stock image-y like smiling actors).

2. A talent dashboard. This will live as a separate microsite; therefore, the design should be consistent with the home page but also be separate. Here, you have some more freedom with the design, but use our overall style and make it look like a user dashboard - very simple and easy to translate for responsive design.

There should be a horizontal menu that includes: "Edit Profile," "Apply for a Job," "WHS" (this will have a drop-down submenu), "My History" (also with a drop-down submenu), and "Contact."

Above that menu should be a place for users to sign in/out. Below the menu will be a welcome message and then a notice board for our updates.

Reason: Still haven't found the perfect design.

Hi designers,

We will make a decision Monday and let you know. Thanks for your submissions!

Industry/Entity Type

Business

Font styles to use
Sans Serif

Colors
33b7a4
f78f20
ffffff

Requirements
Must have
• Please use our current color scheme, fonts, and logo. Attached is our logo and style guidelines. Not included in those style guidelines is the orange we also incorporate into our designs, which is #ff9a00.

Also have a look at http://www.crew4crew.com.au, http://www.crew4crew.com.au/blog, and http://www.friendwall.com/crew4crewrecruitment. We want to take our current look and just modernize it a bit.

```html
<!DOCTYPE html>
<html lang="en">
<head>
<meta charset="utf-8">
<title>Crew4Crew – Recruitment</title>
<link href="https://fonts.googleapis.com/css2?family=Open+Sans:ital,wght@0,300;0,400;0,600;1,300;1,400&display=swap" rel="stylesheet">
<style>
:root{
  --teal:#1f9fb0;
  --teal-btn:#33b7a4;
  --teal-dark:#25a08f;
  --orange:#f78f20;
  --orange-light:#ff9a00;
  --orange-dark:#ee7414;
  --text:#555;
  --text-dark:#444;
  --muted:#999;
  --line:#dcdcdc;
  --footer:#f0f0f0;
  --white:#fff;
}
*{box-sizing:border-box;margin:0;padding:0}
html,body{width:1003px;height:1200px;overflow:hidden}
body{position:relative;background:var(--white);font-family:"Open Sans",Arial,sans-serif;color:var(--text)}
.top-stripe{position:absolute;left:0;top:0;width:1003px;height:5px;background:repeating-linear-gradient(135deg,#ddd 0 1px,#fff 1px 3px)}
.abs{position:absolute}
.brand{left:46px;top:44px;display:flex;align-items:center;gap:12px}
.brand-mark{width:30px;height:30px;background:var(--teal-btn)}
.brand-name{font-size:30px;font-weight:600;color:var(--text-dark);line-height:1}
.contact-block{left:845px;top:22px;font-size:11.5px;line-height:18px;color:var(--text-dark)}
.contact-block .phone{font-size:14px}
.social{display:flex;gap:6px;margin-top:5px}
.social span{width:18px;height:18px;display:block}
.main-nav{left:43px;top:107px;width:917px;height:43px;background:linear-gradient(#fb9b2e,var(--orange-dark));border-radius:2px}
.main-nav a{position:absolute;top:11px;color:var(--white);font-size:16px;text-decoration:none}
.main-nav i{position:absolute;top:0;width:1px;height:43px;background:#d96a10}
.sub-nav{left:45px;top:150px;width:916px;height:37px;background:linear-gradient(#fafafa,#ececec);border:1px solid #e2e2e2;border-top:0}
.sub-nav a{position:absolute;top:9px;font-size:12.5px;font-weight:300;color:var(--text);text-decoration:none}
.sub-nav i{position:absolute;top:0;width:1px;height:36px;background:var(--line)}
.hero{left:45px;top:193px;width:916px;height:275px;background:radial-gradient(circle at 40% 30%,#7ccbe9,#4fa3d4 70%);border:1px solid #cfe3ef}
.dots{position:absolute;left:430px;top:254px;display:flex;gap:5px}
.dots span{width:11px;height:11px;border-radius:50%;background:#fff}
.panel{position:absolute;background:var(--white);border:1px solid var(--line);box-shadow:inset 0 -30px 40px -30px #eee}
.want{left:46px;top:485px;width:665px;height:181px}
.want h2{position:absolute;left:28px;top:18px;font-size:23px;font-weight:300;color:var(--text-dark)}
.cta{position:absolute;top:58px;width:272px;height:92px;border-radius:4px;color:var(--white)}
.cta.job{left:26px;background:linear-gradient(#47c7b2,var(--teal-dark));border-bottom:2px solid #1d8a7b}
.cta.emp{left:323px;background:linear-gradient(#fba23a,var(--orange-dark));border-bottom:2px solid #d25f0a}
.cta h3{position:absolute;left:19px;top:13px;font-size:18px;font-weight:400}
.cta .field{position:absolute;left:19px;top:42px;width:224px;height:26px;background:var(--white);border-radius:3px;font-size:11px;color:#777;padding:5px 11px}
.cta .field svg{position:absolute;right:8px;top:4px}
.side{left:722px;width:238px;height:86px}
.side h3{position:absolute;left:18px;top:11px;font-size:19.5px;font-weight:400;color:var(--text-dark)}
.side p{position:absolute;left:19px;top:38px;font-size:10.5px;font-weight:300;color:var(--muted)}
.btn{position:absolute;left:19px;top:54px;width:78px;height:22px;border-radius:2px;color:var(--white);font-size:10px;text-align:center;line-height:22px}
.btn.teal{background:var(--teal-btn)}
.btn.orange{background:var(--orange-light)}
.listing{left:43px;top:684px;width:670px;height:341px}
.listing h2{position:absolute;left:24px;top:23px;font-size:21.5px;font-weight:400;color:var(--text-dark)}
.col{position:absolute;top:66px;list-style:none}
.col li{height:26.9px;font-size:12.5px;font-weight:300;color:var(--text-dark);padding-left:14px;position:relative}
.col li::before{content:"";position:absolute;left:0;top:5px;width:5px;height:5px;border-right:1px solid #888;border-top:1px solid #888;transform:rotate(45deg)}
.col-sep{position:absolute;top:68px;width:1px;height:230px;background:#eee}
.clients{left:726px;top:683px;width:234px;height:343px}
.clients h2{position:absolute;left:19px;top:11px;font-size:19px;font-weight:400;color:var(--text-dark)}
.clients hr{position:absolute;left:0;top:45px;width:232px;border:0;border-top:1px solid var(--line)}
.quote{position:absolute;left:22px;width:196px;font-size:11.2px;font-style:italic;font-weight:300;line-height:16px;color:var(--muted)}
.quote b{display:block;font-style:normal;font-weight:400;color:var(--text-dark);margin-top:4px}
.badges{left:100px;top:1043px;display:flex;gap:22px;align-items:center}
.badges span{display:block;background:#ccc}
.footer{left:0;top:1137px;width:1003px;height:63px;background:var(--footer)}
.footer p{position:absolute;left:48px;top:24px;font-size:11.5px;font-weight:300;color:#888}
</style>
</head>
<body>
<div class="top-stripe"></div>

<div class="abs brand">
  <span class="brand-mark"></span>
  <span class="brand-name">Crew4Crew</span>
</div>

<div class="abs contact-block">
  <div>48 Harbor Lane #3</div>
  <div>Brookvale 20419 NV</div>
  <div class="phone">555.010.2233</div>
  <div class="social">
    <span style="background:#3b5998"></span>
    <span style="background:#5ec8ef"></span>
    <span style="background:#1a76b3"></span>
    <span style="background:#f68a1e"></span>
  </div>
</div>

<nav class="abs main-nav">
  <a style="left:44px">About</a>
  <i style="left:118px"></i>
  <a style="left:158px">Clients</a>
  <i style="left:240px"></i>
  <a style="left:277px">Candidates</a>
  <i style="left:389px"></i>
  <a style="left:426px">Blog</a>
  <i style="left:494px"></i>
  <a style="left:529px">Contact</a>
</nav>

<nav class="abs sub-nav">
  <a style="left:27px">What we do</a>
  <i style="left:107px"></i>
  <a style="left:121px">How we Work</a>
  <i style="left:213px"></i>
  <a style="left:225px">Where We are</a>
  <i style="left:318px"></i>
  <a style="left:329px">About Us</a>
  <i style="left:396px"></i>
</nav>

<div class="abs hero" role="img" aria-label="Banner illustration of white rings and bubbles with a blue leafy plant on a sky blue background">
  <div class="dots"><span></span><span></span><span></span><span></span></div>
</div>

<section class="panel want">
  <h2>I want to</h2>
  <div class="cta job">
    <h3>Find a job</h3>
    <div class="field">type your job..
      <svg width="18" height="18" viewBox="0 0 18 18"><circle cx="9" cy="9" r="8" fill="none" stroke="#888" stroke-width="1.5"/><path d="M5 9h8M10 6l3 3-3 3" fill="none" stroke="#888" stroke-width="1.5"/></svg>
    </div>
  </div>
  <div class="cta emp">
    <h3>Find Employees</h3>
    <div class="field">type your employee
      <svg width="18" height="18" viewBox="0 0 18 18"><circle cx="9" cy="9" r="8" fill="none" stroke="#888" stroke-width="1.5"/><path d="M5 9h8M10 6l3 3-3 3" fill="none" stroke="#888" stroke-width="1.5"/></svg>
    </div>
  </div>
</section>

<section class="panel side" style="top:485px">
  <h3>Talent Portal</h3>
  <p>Aliquam nec erat at purus cursus interd</p>
  <div class="btn teal">CLICK HERE</div>
</section>
<section class="panel side" style="top:580px">
  <h3>Salarysite</h3>
  <p>Aliquam nec erat at purus cursus interd</p>
  <div class="btn orange">CLICK HERE</div>
</section>

<section class="panel listing">
  <h2>Phasellus felis dolor scelerisque</h2>
  <ul class="col" style="left:24px">
    <li>Praesent elementum</li><li>Malesuada nec ultricies</li><li>Sit amet porttitor</li><li>Mattis enim</li><li>Massa libero interdum</li><li>Nec interdum vel</li><li>Clandit sed nulla</li><li>Ullamcorper est</li><li>Eget tempor cursus</li>
  </ul>
  <div class="col-sep" style="left:204px"></div>
  <ul class="col" style="left:247px">
    <li>Praesent elementum</li><li>Malesuada nec ultricies</li><li>Sit amet porttitor</li><li>Mattis enim</li><li>Massa libero interdum</li><li>Nec interdum vel</li><li>Clandit sed nulla</li><li>Ullamcorper est</li><li>Eget tempor cursus</li>
  </ul>
  <div class="col-sep" style="left:428px"></div>
  <ul class="col" style="left:478px">
    <li>Praesent elementum</li><li>Malesuada nec ultricies</li><li>Sit amet porttitor</li><li>Mattis enim</li><li>Massa libero interdum</li><li>Nec interdum vel</li><li>Clandit sed nulla</li><li>Ullamcorper est</li><li>Eget tempor cursus</li>
  </ul>
</section>

<aside class="panel clients">
  <h2>What Clients Says</h2>
  <hr>
  <div class="quote" style="top:62px">Phasellus felis dolor, scelerisque a, tempus eget, lobortis id, libero. Donec scelerisque leo ac risus Praesent sit<b>By Author Name</b></div>
  <div class="quote" style="top:137px">Donec scelerisque leo ac risus. Praesent sit amet est. In dictum, dolor eu dictum porttitor, enim felis viverra mi, eget luctus massa purus quis odio. Etiam nulla massa, pharetra facilisis<b>By Author Name</b></div>
  <div class="quote" style="top:252px">Phasellus felis dolor, scelerisque a, tempus eget, lobortis id, libero. Donec scelerisque leo ac risus Praesent sit<b>By Author Name</b></div>
</aside>

<div class="abs badges">
  <span style="width:46px;height:46px;background:#333"></span>
  <span style="width:62px;height:28px;background:#bbb"></span>
  <span style="width:66px;height:56px;border-radius:50%;background:#f2c04a"></span>
  <span style="width:54px;height:40px;background:#c9ccd6"></span>
  <span style="width:84px;height:44px;background:#e07a3a"></span>
  <span style="width:78px;height:46px;border-radius:50%;background:#c94b4b"></span>
  <span style="width:62px;height:30px;background:#1e8a55"></span>
  <span style="width:66px;height:48px;background:#888"></span>
  <span style="width:32px;height:66px;background:#2a3a8c"></span>
  <span style="width:78px;height:36px;background:#555"></span>
</div>

<footer class="abs footer">
  <p>© 2013 Company Name.&nbsp; All right reserved.&nbsp; Privacy Policy</p>
</footer>
</body>
</html>
```